Social Media Infographic for White Paper

Am working on a white paper on social media use by C-Suite Executives, and hope to include some infographics. I would like some help designing the first infographic.

The master bit of information is that "66% of C-Suite Executives use social media for professional purpose."

Within that 66%
-70% post original content on a daily/weekly basis
-13% of professional users are lurkers
-40% plan to use social media even more in the future

After initial design will need to two versions of the infographic, one listing the source at the bottom in small print (Source: 2017 Venmoor Partners Executive Social Media Study), the other one with no source information.

Infographic design should be complimentary with my website: www.venmoorpartners.example, but use of green should be very limited, if at all.

Target Market(s)

New media, C-Suite Executives, Executive Coaches

Industry/Entity Type

Management Consulting

Font styles to use
Sans Serif

Requirements
Must have
• Infographic with data displayed in a easy to understand format that tells the story of C-Suite Executives that participate in social media for professional purposes.
Nice to have
• Complements website design - www.venmoor.example.
Should not have
• Limit use of green from website logo, which can be overpowering. Some is ok, but not too much

```html
<!DOCTYPE html>
<html lang="en">
<head>
<meta charset="utf-8">
<title>C-Suite Executives on Social Media</title>
<link rel="stylesheet" href="https://fonts.googleapis.com/css2?family=Oswald:wght@300&family=Nunito+Sans:ital,wght@0,400;0,700;0,800;1,400;1,800&display=swap">
<style>
  :root {
    --green: #5e9c3b;
    --ring-grey: #d3d4d5;
    --text: #555a5e;
    --text-soft: #6a6e72;
    --ink: #2b2b2b;
    --figure: #e4e7ea;
    --band: #e3e6e9;
    --paper: #ffffff;
  }
  * { margin: 0; padding: 0; box-sizing: border-box; }
  html, body { width: 1200px; height: 927px; overflow: hidden; background: var(--paper); }
  .infographic {
    position: relative; width: 1200px; height: 927px; overflow: hidden;
    font-family: "Nunito Sans", sans-serif; color: var(--text);
  }
  .figure {
    position: absolute; top: 56px; height: 768px;
    background: linear-gradient(180deg, #eceef0 0%, var(--figure) 60%);
  }
  .figure--left { left: 0; width: 104px; border-top-right-radius: 60px; }
  .figure--right { right: 0; width: 210px; border-top-left-radius: 80px; }

  .brand { position: absolute; left: 782px; top: 26px; }
  .brand__mark {
    position: absolute; left: 0; top: 0; width: 60px; height: 60px;
    border-radius: 50%; background: var(--green);
  }
  .brand__name {
    position: absolute; left: 70px; top: 6px; width: 160px;
    font-weight: 800; font-size: 23px; line-height: 24px; color: var(--ink);
  }
  .brand__url {
    position: absolute; left: 768px; top: 92px;
    font-style: italic; font-size: 16px; letter-spacing: 0.5px; color: var(--ink);
  }

  .headline__figure {
    position: absolute; left: 440px; top: 52px; width: 290px; text-align: center;
    font-family: "Oswald", sans-serif; font-weight: 300; font-size: 176px; line-height: 1;
    color: var(--green); letter-spacing: -4px;
  }
  .headline__text {
    position: absolute; left: 300px; top: 246px; width: 560px; text-align: center;
    font-size: 35px; line-height: 44px; color: var(--text); letter-spacing: 0.3px;
  }

  .channels { position: absolute; left: 408px; top: 358px; display: flex; gap: 16px; }
  .channels span { width: 30px; height: 30px; border-radius: 6px; background: #e6e9ee; }

  .connector { position: absolute; left: 0; top: 0; }

  .stat { position: absolute; top: 480px; }
  .stat__value {
    position: absolute; top: 166px; width: 200px; text-align: center;
    font-family: "Oswald", sans-serif; font-weight: 300; font-size: 60px; line-height: 1;
    color: var(--green); letter-spacing: -2px;
  }
  .stat__label {
    position: absolute; top: 240px; width: 300px;
    font-size: 22px; line-height: 29px; color: var(--text-soft); letter-spacing: 0.4px;
  }
  .stat__label strong { font-weight: 800; font-style: italic; color: var(--text); }

  .divider {
    position: absolute; top: 540px; height: 168px; width: 0;
    border-left: 2px dashed #c9cbcd;
  }

  .source-band {
    position: absolute; left: 0; top: 824px; width: 1200px; height: 103px; background: var(--band);
  }
  .source-band__text {
    position: absolute; left: 0; top: 22px; width: 1200px; text-align: center;
    font-size: 34px; color: #111; letter-spacing: 0.3px;
  }
  .source-band__rule {
    position: absolute; left: 154px; top: 74px; width: 930px; height: 1px; background: #f6f7f8;
  }
</style>
</head>
<body>
<main class="infographic">
  <div class="figure figure--left" role="img" aria-label="Silhouette of an executive reading a tablet with social network symbols floating above"></div>
  <div class="figure figure--right" role="img" aria-label="Silhouette of an executive holding a tablet with social network symbols floating above"></div>

  <div class="brand">
    <span class="brand__mark"></span>
    <span class="brand__name">Venmoor Partners</span>
  </div>
  <p class="brand__url">www.venmoorpartners.example</p>

  <h1 class="headline__figure">66%</h1>
  <p class="headline__text">of C-Suite Executives use social media for professional purpose.</p>

  <div class="channels" aria-label="Social networks">
    <span></span><span></span><span></span><span></span><span></span><span></span><span></span>
  </div>

  <svg class="connector" width="1200" height="927" viewBox="0 0 1200 927" aria-hidden="true">
    <defs>
      <linearGradient id="connector-fade" x1="0" x2="1" y1="0" y2="0">
        <stop offset="0" stop-color="#6d6f72" stop-opacity="0"/>
        <stop offset="0.25" stop-color="#6d6f72" stop-opacity="0.8"/>
        <stop offset="0.75" stop-color="#6d6f72" stop-opacity="0.8"/>
        <stop offset="1" stop-color="#6d6f72" stop-opacity="0"/>
      </linearGradient>
      <radialGradient id="dial-face" cx="0.45" cy="0.4" r="0.6">
        <stop offset="0" stop-color="#ffffff"/>
        <stop offset="1" stop-color="#e2e3e4"/>
      </radialGradient>
    </defs>
    <path d="M278 454 Q300 420 350 420 L830 420 Q880 420 892 442" fill="none" stroke="url(#connector-fade)" stroke-width="4"/>
    <line x1="588" y1="420" x2="588" y2="464" stroke="#6d6f72" stroke-width="5"/>

    <!-- dial: original content -->
    <g transform="translate(269 560)">
      <circle r="70" fill="none" stroke="var(--ring-grey)" stroke-width="9"/>
      <circle r="60" fill="none" stroke="var(--green)" stroke-width="12" stroke-dasharray="264 377" transform="rotate(144)"/>
      <circle r="48" fill="url(#dial-face)"/>
      <g fill="none" stroke="#cfd0d1" stroke-width="2">
        <path d="M-16 -22 H6 L14 -14 V22 H-16 Z"/>
        <path d="M-10 -10 H6 M-10 -3 H6 M-10 4 H0"/>
        <path d="M-8 14 q6 -8 10 0 t10 -2"/>
        <path d="M20 -18 L4 8"/>
      </g>
    </g>

    <!-- dial: lurkers -->
    <g transform="translate(588 554)">
      <circle r="70" fill="none" stroke="var(--ring-grey)" stroke-width="9"/>
      <circle r="58" fill="none" stroke="var(--green)" stroke-width="12" stroke-dasharray="49 377" transform="rotate(-65)"/>
      <circle r="48" fill="url(#dial-face)"/>
      <path d="M-32 0 Q0 -26 32 0 Q0 26 -32 0 Z" fill="#d9dadb"/>
      <circle r="13" fill="#f2f2f2"/>
      <circle r="7" fill="#d0d1d2"/>
    </g>

    <!-- dial: future growth -->
    <g transform="translate(901 556)">
      <circle r="70" fill="none" stroke="var(--ring-grey)" stroke-width="9"/>
      <circle r="60" fill="none" stroke="var(--green)" stroke-width="12" stroke-dasharray="151 377" transform="rotate(-90)"/>
      <circle r="48" fill="url(#dial-face)"/>
      <g fill="#d8d9da">
        <rect x="-20" y="8" width="9" height="14"/>
        <rect x="-7" y="-2" width="9" height="24"/>
        <rect x="6" y="-14" width="9" height="36"/>
      </g>
      <path d="M-28 2 Q-10 -8 0 -24" fill="none" stroke="#d0d1d2" stroke-width="3"/>
      <path d="M-6 -24 L2 -28 L1 -18" fill="none" stroke="#d0d1d2" stroke-width="3"/>
    </g>
  </svg>

  <div class="divider" style="left:443px"></div>
  <div class="divider" style="left:749px"></div>

  <section class="stat" style="left:169px">
    <p class="stat__value">70%</p>
    <p class="stat__label" style="left:-15px">post <strong>original content</strong><br>on a daily/weekly basis</p>
  </section>
  <section class="stat" style="left:492px">
    <p class="stat__value">13%</p>
    <p class="stat__label" style="left:13px">of professional<br>users are <strong>lurkers</strong></p>
  </section>
  <section class="stat" style="left:815px">
    <p class="stat__value">40%</p>
    <p class="stat__label" style="left:-18px">plan to use social media<br>even more in the future</p>
  </section>

  <footer class="source-band">
    <p class="source-band__text">Source: 2017 Venmoor Partners Executive Social Media Study</p>
    <span class="source-band__rule"></span>
  </footer>
</main>
</body>
</html>
```